New start-up venture BrightPlate needs eye-catching, bright, vibrant catering menu design.

BrightPlate is looking for a tri-fold menu design (6 total pages) for our start-up catering business in Southern New Jersey. Designs should be informative, colorful, appealing, and represent the overall BrightPlate concept:

“The vision of BRIGHTPLATE is to provide high quality organic nutrient dense food, juices, and snacks at affordable prices in a positive, fun, and educational environment inspiring a revolution of optimal health and well-being.”

Brightplate is a Revolutionary catering/take-out concept offering a simple, customizable menu for customers who appreciate a modern approach to traditional food but also place a high priority on health, taste, affordability, and convenience.

Brightplate primary market consists of on-the-go health conscious eaters and those with food allergies. They are deliberate about their eating choices, value quality and convenience, and are willing to pay more for those qualities. We provide Real Food for Real People in the rapidly growing segment of the health conscious dining industry.

• The tri-fold (6 total pages) catering menu brochure must include our name and We Are BrightPlate logo that has been attached.
You are free to pick and choose our personal pictures of salads, juices, snacks, etc. which are also attached.
The list of various BrightPlate benefits on the back page of brochure (also added to the uploaded files).
Actual menu items and descriptions (uploaded file section)
Unique, easy to read (legible), fun, and eye-catching font. Please include the following saying, "Real Food for Real People"

Front cover (First page) should be the We Are BrightPlate logo and space for contact information (You can choose to include pictures of various BrightPlate, fruits, and vegetables or choose from our personal pictures that are attached)
Pages 2 through 5 should each include our various menu items - all information has been attached:
(Page 2 - Information/pictures with names and descriptions of the BrightPlates smoothies, Page 3 - Information/pictures on the Fresh organic juices with names and descriptions, Page 4 - Information/pictures on the Zest Loaded Bowls with names and descriptions, Page 5 - Information/pictures on additional packaged and prepared menu items)
Page 6 (Back cover - the attached list of various BrightPlates benefits - maybe a picture of the We Are BrightPlate spinner game - attached file)
• It would be nice for the brochure to incorporate the colors in the BrightPlate seed of life logo and/or greens, oranges (colors of vegetables). Should you come across a stunning photograph that would benefit brochure, we would entertain that idea of including that photo.
• Too much open or empty space.

```html
<!DOCTYPE html>
<html lang="en">
<head>
<meta charset="utf-8">
<title>We Are BrightPlate – Food Menu</title>
<link href="https://fonts.googleapis.com/css2?family=Josefin+Sans:wght@300;400;600&family=Open+Sans:ital,wght@0,400;0,600;1,400&display=swap" rel="stylesheet">
<style>
  :root {
    --yellow: #f3c916;
    --peach: #f6b98a;
    --orange: #ee8a1f;
    --orange-deep: #e06d12;
    --charcoal: #2f3032;
    --sky: #36b6e8;
    --maroon: #7a1d12;
    --maroon-deep: #5e140c;
    --brown: #4a2614;
    --red: #e8352a;
    --purple: #5b3a8c;
    --ink: #3a2a1e;
    --white: #ffffff;
  }
  * { box-sizing: border-box; margin: 0; padding: 0; }
  html, body { width: 1200px; height: 848px; overflow: hidden; background: #ffffff; }
  .brochure { position: relative; width: 1200px; height: 848px; overflow: hidden; font-family: "Open Sans", Arial, sans-serif; }

  .panel { position: absolute; top: 0; height: 848px; }
  .panel--packaged { left: 0; width: 456px; background: linear-gradient(var(--yellow) 0 276px, var(--peach) 276px); }
  .panel--benefits { left: 456px; width: 344px; background: var(--yellow); }
  .panel--cover { left: 800px; width: 400px; background: var(--yellow); border-left: 1px solid rgba(0,0,0,.08); }

  .photo { position: absolute; border-radius: 50%; border: 5px solid var(--white); }

  /* Packaged panel */
  .badge { position: absolute; left: 124px; top: 12px; width: 204px; height: 204px; border-radius: 50%;
    background: radial-gradient(circle at 40% 35%, #f39a3a, var(--orange-deep)); color: var(--white);
    font-family: "Josefin Sans", Arial, sans-serif; font-weight: 300; }
  .badge__text { position: absolute; left: 0; width: 176px; top: 62px; text-align: center; }
  .badge__line { font-size: 27px; line-height: 32px; }
  .badge__amp { position: absolute; left: 160px; top: 78px; font-size: 40px; line-height: 40px; }
  .badge__sub { font-size: 19px; letter-spacing: 1px; margin-top: 2px; }
  .photo--salad { left: 12px; top: 140px; width: 246px; height: 222px; border-radius: 50%; background: radial-gradient(circle, #e6d6a0, #b7a35e 60%, #5d8a35); }
  .photo--crackers { left: 232px; top: 252px; width: 134px; height: 134px; background: radial-gradient(circle, #b59a78, #6e5d55 70%, #443a45); }

  .menu-list { position: absolute; left: 54px; width: 292px; color: var(--ink); }
  .menu-list--packaged { top: 411px; }
  .menu-list--prepared { top: 651px; }
  .menu-list__title { display: flex; align-items: center; gap: 8px; justify-content: center; color: var(--purple);
    font-size: 11.5px; font-weight: 600; text-transform: uppercase; letter-spacing: .3px; }
  .menu-list__title::before, .menu-list__title::after { content: ""; flex: 1; height: 2px; background: linear-gradient(90deg, transparent, var(--purple)); }
  .menu-list__title::after { background: linear-gradient(90deg, var(--purple), transparent); }
  .menu-list__sub { text-align: center; color: var(--purple); font-size: 10px; margin-bottom: 10px; }
  .menu-item { list-style: none; font-size: 12px; padding: 6px 0 8px; border-bottom: 1px dashed rgba(90,60,40,.55); }
  .menu-item__desc { display: block; font-style: italic; font-size: 11.5px; line-height: 1.35; }

  /* Benefits panel */
  .benefits { position: absolute; left: 0; top: 0; width: 290px; height: 730px; background: var(--charcoal); text-align: center; color: var(--white); }
  .benefits__mark { width: 78px; height: 78px; border-radius: 50%; margin: 26px auto 8px; background: radial-gradient(circle, #f4f4f4, #9a9a9a); }
  .benefits__title { font-family: "Josefin Sans", Arial, sans-serif; font-weight: 400; color: var(--sky); font-size: 34px; line-height: 33px; }
  .benefits__list { list-style: none; margin: 14px 0 0; font-size: 12.6px; line-height: 17.1px; white-space: nowrap; }
  .benefits__list li::before { content: "• "; }
  .photo--spinner { left: 6px; top: 622px; width: 276px; height: 276px; border: 0; background: radial-gradient(circle, #f3ead6 0 36%, #c2391e 37%, #8a1d10 80%); }

  /* Cover panel */
  .cover__band { position: absolute; left: 0; top: 0; width: 400px; height: 156px; background: linear-gradient(var(--maroon), var(--maroon-deep)); color: var(--white); text-align: center; padding-top: 24px; }
  .cover__we { font-family: "Josefin Sans", Arial, sans-serif; font-weight: 400; font-size: 40px; line-height: 46px; }
  .cover__name { font-family: "Josefin Sans", Arial, sans-serif; font-weight: 400; font-size: 41px; line-height: 48px; margin-top: 12px; }
  .cover__photo { position: absolute; left: 0; top: 162px; width: 400px; height: 330px; background: var(--orange); border-bottom-right-radius: 10px; }
  .cover__photo-fill { position: absolute; left: 10px; top: 6px; right: 0; bottom: 14px; border-bottom-left-radius: 60px; background: radial-gradient(ellipse at 40% 45%, #d85b2a, #a98a5c 55%, #cfc7b7); }
  .photo--juice { left: 222px; top: 356px; width: 200px; height: 216px; border: 6px solid var(--orange); background: radial-gradient(circle at 50% 60%, #f46a2a, #e43f16 60%, #d9c9b6); }
  .cover__badge { position: absolute; left: 110px; top: 442px; width: 172px; height: 172px; border-radius: 50%; background: var(--brown); color: var(--white);
    font-family: "Josefin Sans", Arial, sans-serif; font-weight: 300; text-align: center; padding-top: 50px; }
  .cover__badge-big { font-size: 46px; line-height: 46px; }
  .cover__badge-small { font-size: 22px; margin-top: 4px; }
  .cover__tagline { position: absolute; left: 0; width: 400px; top: 658px; text-align: center; color: var(--red); font-family: "Open Sans", Arial, sans-serif; font-size: 23px; line-height: 31px; }
  .cover__rule { position: absolute; left: 64px; width: 272px; top: 731px; height: 1px; background: var(--brown); }
  .contact { position: absolute; left: 0; width: 400px; top: 740px; text-align: center; color: var(--ink); font-size: 11px; line-height: 14px; font-style: normal; }
  .contact__name { font-size: 15px; line-height: 20px; }
</style>
</head>
<body>
<main class="brochure">

  <section class="panel panel--packaged">
    <div class="photo photo--salad" role="img" aria-label="Photo of quinoa salad with mango, cranberries and basil"></div>
    <div class="photo photo--crackers" role="img" aria-label="Photo of multi-grain and sweet potato crackers"></div>
    <div class="badge">
      <div class="badge__text">
        <div class="badge__line">PACKAGED</div>
        <div class="badge__line">PREPARED</div>
        <div class="badge__sub">MENU</div>
      </div>
      <span class="badge__amp">&amp;</span>
    </div>

    <div class="menu-list menu-list--packaged">
      <h2 class="menu-list__title">Additional Packaged</h2>
      <p class="menu-list__sub">Menu Items</p>
      <ul>
        <li class="menu-item">Mellow Bars and Granola Cereals</li>
        <li class="menu-item">BrightPlates Cereals</li>
        <li class="menu-item">Field Story Multi-Grain and Sweet Potato Chips</li>
        <li class="menu-item">Early Harvest Sea Salt and Moonlit Berry Chips</li>
        <li class="menu-item">Leaf Forward Greens and Chocolate Energy Bars</li>
        <li class="menu-item">Pine Ridge Nut Clusters</li>
      </ul>
    </div>

    <div class="menu-list menu-list--prepared">
      <h2 class="menu-list__title">Additional Prepared</h2>
      <p class="menu-list__sub">Menu Items</p>
      <ul>
        <li class="menu-item">Quinoa with Zucchini and Squash
          <span class="menu-item__desc">Prepared in olive oil, with pepperoncini and various spices</span></li>
        <li class="menu-item">Lean ground Turkey meat quinoa tacos
          <span class="menu-item__desc">Prepared in olive oil with pepperoncini and various<br>spices</span></li>
      </ul>
    </div>
  </section>

  <section class="panel panel--benefits">
    <div class="photo photo--spinner" role="img" aria-label="Photo of red apples behind the We Are BrightPlate spinner game"></div>
    <div class="benefits">
      <div class="benefits__mark"></div>
      <h2 class="benefits__title">BRIGHTPLATE<br>BENEFIT</h2>
      <ul class="benefits__list">
        <li>Both a food and medicine</li>
        <li>Superior source of anti-oxidants</li>
        <li>Nutrient dense and calorie sparse</li>
        <li>No known negative properties or<br>side effects</li>
        <li>Protects and Heals the Body</li>
        <li>Increases Energy</li>
        <li>Improves Overall Health</li>
        <li>Nourishes the Entire Body</li>
        <li>Increases Life Expectancy</li>
        <li>Reduce Body Fat</li>
        <li>Boosts Mood</li>
        <li>Reduces Stress</li>
        <li>Aids Digestion</li>
        <li>Improves Productivity</li>
        <li>Corrects Imbalances</li>
        <li>Reduces Inflammation</li>
        <li>Boosts and Supports the Immune<br>System</li>
        <li>Prevents and Reverses Chronic<br>Disease</li>
        <li>Slows Down the Aging Process</li>
        <li>Improves the severity and<br>symptoms of major diseases</li>
        <li>Cleanses and Detoxifies the Body</li>
      </ul>
    </div>
  </section>

  <section class="panel panel--cover">
    <header class="cover__band">
      <div class="cover__we">We Are</div>
      <h1 class="cover__name">BRIGHTPLATE</h1>
    </header>
    <div class="cover__photo">
      <div class="cover__photo-fill" role="img" aria-label="Photo of a large wooden bowl of fresh salad with bowls of seeds on a table"></div>
    </div>
    <div class="photo photo--juice" role="img" aria-label="Photo of a glass of fresh orange-red juice"></div>
    <div class="cover__badge">
      <div class="cover__badge-big">FOOD</div>
      <div class="cover__badge-small">MENU</div>
    </div>
    <p class="cover__tagline">Let Food Be Thy Medicine<br>and Medicine Be Thy Food</p>
    <div class="cover__rule"></div>
    <address class="contact">
      <div class="contact__name">BrightPlate Avenue</div>
      <div>Lumen Street NA 114</div>
      <div>North Vellmar</div>
      <div>5550-1234-8876</div>
    </address>
  </section>

</main>
</body>
</html>
```